Design a styled business card for an intimacy and attachment psychologist

I am a Psychologist providing online therapy to patients across the United States. My work is interpersonal and emotion-focused, with an emphasis on the client-therapist relationship. My primary areas of work are very personal, including sexuality and gender, abuse and trauma, and grief and loss. My target audience will be adults of all ages 18+.
My business card should convey a warm and inviting feeling of professionalism that is also casual and comfortable.
The front should be fairly simple and professional, consisting of:
- My name, Dr. Rosalind Petrakis
- My title, Licensed Psycholigist
- My logo
On either the front or the back, my contact information should be listed:
- ros@drrospetrakis.example
- 555.014.7788
- drrospetrakis.example
On the rear, I would like a description of the areas that I specialize in. This can be formatted in any way that appears stylistically interesting.
Individual and Couples
Relationships and Infidelity
Sexual Health & Aging
Gender Identity & Sexual Orientation
Abuse and Trauma
Sexual Compulsivity & Addiction
Sexual Dysfunction
Target Market(s)
My target audience will be adults of all ages 18+.
Industry/Entity Type
Psychology
Contact Information for Business Card
The front should be fairly simple and professional, consisting of: - My name, Dr. Rosalind Petrakis - My title, Licensed Psycholigist - My logo On either the front or the back, my contact information should be listed: - ros@drrospetrakis.example - 555.014.7788 - drrospetrakis.example On the rear, I would like a description of the areas that I specialize in. This can be formatted in any way that appears stylistically interesting. Individual and Couples Relationships and Infidelity Sexual Health & Aging Gender Identity & Sexual Orientation Abuse and Trauma Sexual Compulsivity & Addiction Sexual Dysfunction
- Follow brand guide

```html
<!DOCTYPE html>
<html lang="en">
<head>
<meta charset="utf-8">
<title>Dr. Rosalind Petrakis — Business Card</title>
<link rel="stylesheet" href="https://fonts.googleapis.com/css2?family=Cinzel:wght@400;500&family=Lato:wght@400;700&display=swap">
<style>
  :root {
    --navy: #2b2450;
    --teal: #4fd3b5;
    --mint: #96e6d5;
    --mint-pale: #cdf2ea;
    --orange: #fca713;
    --red: #f2434a;
    --purple: #a96bd1;
    --white: #ffffff;
    --backdrop: #e8e4df;
  }
  * { box-sizing: border-box; margin: 0; padding: 0; }
  html, body { width: 1200px; height: 977px; overflow: hidden; }
  body {
    background: var(--backdrop);
    font-family: "Lato", Arial, sans-serif;
    color: var(--navy);
    position: relative;
  }
  .card {
    position: absolute;
    left: 220px;
    width: 760px;
    height: 434px;
    background: var(--white);
    border-radius: 22px;
    overflow: hidden;
    box-shadow: 0 6px 18px rgba(40, 30, 20, .18);
  }
  .card--back { top: 36px; }
  .card--front { top: 506px; }

  /* Back: specialties */
  .wave { position: absolute; inset: 0; width: 100%; height: 100%; }
  .brand {
    position: absolute;
    left: 64px;
    top: 62px;
    display: flex;
    align-items: center;
    gap: 26px;
  }
  .brand__mark {
    width: 124px; height: 124px;
    border-radius: 50%;
    background: var(--mint);
    border: 7px solid var(--navy);
    flex: none;
  }
  .brand__name {
    font-family: "Cinzel", Georgia, serif;
    font-weight: 400;
    color: var(--navy);
    line-height: .92;
  }
  .brand__name .line-dr { font-size: 26px; display: block; margin-bottom: 6px; letter-spacing: 1px; }
  .brand__name .line-big { font-size: 52px; display: block; letter-spacing: 1px; }

  .specialties {
    position: absolute;
    right: 46px;
    bottom: 30px;
    width: 520px;
    color: var(--white);
    font-size: 17px;
    line-height: 1.55;
    text-align: right;
  }
  .specialties .dot {
    display: inline-block;
    width: 9px; height: 9px;
    border-radius: 50%;
    margin: 0 6px 1px;
    vertical-align: middle;
  }
  .dot--teal { background: var(--teal); }
  .dot--red { background: var(--red); }
  .dot--orange { background: var(--orange); }
  .dot--purple { background: var(--purple); }

  /* Front: identity */
  .emblem-field {
    position: absolute;
    left: -150px;
    top: 24px;
    width: 560px;
    height: 560px;
    border-radius: 50%;
    border: 16px solid var(--navy);
    background: radial-gradient(circle at 60% 40%, var(--mint-pale), var(--mint) 55%, var(--teal));
  }
  .identity {
    position: absolute;
    left: 468px;
    top: 62px;
    width: 280px;
  }
  .identity__name {
    font-family: "Cinzel", Georgia, serif;
    font-weight: 400;
    font-size: 40px;
    line-height: .92;
    color: var(--navy);
  }
  .identity__title {
    font-size: 22px;
    color: var(--teal);
    margin-top: 8px;
  }
  .identity__rule {
    width: 44px;
    height: 4px;
    background: var(--navy);
    margin: 22px 0 18px;
  }
  .contacts { list-style: none; font-size: 18px; color: var(--navy); }
  .contacts li { display: flex; align-items: center; gap: 10px; margin-bottom: 8px; }
  .contacts .phone { font-weight: 700; font-size: 21px; }
  .contacts svg { width: 16px; height: 16px; flex: none; }
</style>
</head>
<body>

<section class="card card--back" aria-label="Card back: areas of specialty">
  <svg class="wave" viewBox="0 0 760 434" preserveAspectRatio="none" aria-hidden="true">
    <g fill="none" stroke-linecap="round">
      <path transform="translate(0,-40)" d="M0,330 C220,322 380,270 480,190 C570,120 660,108 760,118" stroke="var(--purple)" stroke-width="4"/>
      <path transform="translate(0,-28)" d="M0,330 C220,322 380,270 480,190 C570,120 660,108 760,118" stroke="var(--orange)" stroke-width="10"/>
      <path transform="translate(0,-17)" d="M0,330 C220,322 380,270 480,190 C570,120 660,108 760,118" stroke="var(--red)" stroke-width="6"/>
      <path transform="translate(0,-8)" d="M0,330 C220,322 380,270 480,190 C570,120 660,108 760,118" stroke="var(--teal)" stroke-width="7"/>
    </g>
    <path d="M0,330 C220,322 380,270 480,190 C570,120 660,108 760,118 L760,434 L0,434 Z" fill="var(--navy)"/>
  </svg>

  <div class="brand">
    <div class="brand__mark" aria-hidden="true"></div>
    <div class="brand__name">
      <span class="line-dr">Dr.</span>
      <span class="line-big">Rosalind</span>
      <span class="line-big">Petrakis</span>
    </div>
  </div>

  <p class="specialties">
    Individual &amp; Couples<span class="dot dot--teal"></span>Relationships &amp; Infidelity<br>
    Sexual Health &amp; Aging<span class="dot dot--red"></span>Gender Identity &amp; Sexual Orientation<br>
    Abuse &amp; Trauma<span class="dot dot--orange"></span>Sexual Compulsivity &amp; Addiction<span class="dot dot--purple"></span>Sexual Dysfunction
  </p>
</section>

<section class="card card--front" aria-label="Card front: name and contact">
  <div class="emblem-field" role="img" aria-label="Large decorative emblem area in mint and teal tones"></div>

  <div class="identity">
    <h1 class="identity__name">Dr.<br>Rosalind<br>Petrakis</h1>
    <p class="identity__title">Licensed Psycholigist</p>
    <div class="identity__rule"></div>
    <ul class="contacts">
      <li class="phone">
        <svg viewBox="0 0 16 16" aria-hidden="true"><path d="M4 1.5l2.3 3-1.4 1.6a8 8 0 0 0 5 5l1.6-1.4 3 2.3-1.3 2.2C8.5 14.5 1.5 7.5 1.8 2.8z" fill="var(--red)"/></svg>
        555.014.7788
      </li>
      <li>
        <svg viewBox="0 0 16 16" aria-hidden="true"><rect x="1" y="3" width="14" height="10" rx="1" fill="var(--orange)"/><path d="M1.5 3.5L8 9l6.5-5.5" fill="none" stroke="var(--white)" stroke-width="1.4"/></svg>
        ros@drrospetrakis.example
      </li>
      <li>
        <svg viewBox="0 0 16 16" aria-hidden="true"><circle cx="8" cy="8" r="7" fill="var(--purple)"/><path d="M1 8h14M8 1c-3 3.5-3 10.5 0 14M8 1c3 3.5 3 10.5 0 14" fill="none" stroke="var(--white)" stroke-width="1"/></svg>
        drrospetrakis.example
      </li>
    </ul>
  </div>
</section>

</body>
</html>
```